Pruett Design & Millwork needs a web presence. Looking for a unique Design so please submit an idea.

In brief, you should know the following about me: My company was established in 2001 and had been responsible for providing reasonable CAD Design and Custom Millwork ever since. My specialty is in the area Architectural CAD Design, Fabrication of Custom Millwork and Mouldings on a partime basis. Drawings and estimates done at a very reasonable cost. I look forward to working on your next project. Thanks in Advance, Glen 
I would like one page to show thumbnails linked to some of past millwork projects and another page with thumbnails linking to some of my house designs. I assume last page will have contact information accessed from a link on home page. I already had a logo designed which I can supply you with to design home page around. As I indicated I have a regular full time job and do this for additional income and will move to full time when I have enough business.

I have attached the logo I had designed in a couple different colors. I have also uploaded some PDF's of files that I also considered before choosing the RED LOGO to give an ideas of how we could tweak the logo to better fit the website if need be. Text is wrong in those.

Thanks,
Glen

I added my logo as a PDF side there seems to be a problem with scaling loge with the other file. Hope this helps.

Glen

Evening,
I will be hosting this site on servquill. Its looks like it will get launched with wordpress?  What will be involved from getting your design up so I can upload project pictures and and text to areas you have set aside? I am also going to upload a couple jpg of a couple recent projects so you can put in so I can get a feel of what they will look like. Thanks for all your work to date! Glen

I am not seeing alot of design variations or even many designers in fact. Is there something more from me you need? Do you need me to extend deadline?

Reason: It appears that your need some more time to submit some design changes. I will choose a design next week after changes have been submitted. Thanks for your time. Glen

Reason: Designers needs a couple days to submit some last minute changes. Thanks for all your submissions! Glen

Reason: Some last minute designs that I need to look at and give feedback on. I want to thank everyone for their designs and patience. Thanks again, Glen

Evening All,

Upon discussion with a couple of the designers I want the design done in Word Press and I have increased budget the amount they said they would need to do it for. Thanks for all submissions so far but I am still looking for the special one that stands out among the rest! Glen

I will not be extending deadline and choosing designer tomorrow morning so if you have anything else to add please do so tonight. Thanks for all your submissions. Glen

Target Market(s)

Millwork projects will be generally local where as CAD Design Projects could be emailed anywhere. Probably more USA but who knows.

Industry/Entity Type

House

Font styles to use
Other font styles liked:
• Eras Medium ITC, Calibri or Designers choice.

Requirements
Must have
• Must tie in my logo on Homepage at least. Could even be somewhat transparent in background? I will let the designer work that out.
Nice to have
• Page to point to current and past Design projects on one page and millwork on another.
Should not have
• Target a large Corporate or Global environment since it is a small business right now.

```html
<!DOCTYPE html>
<html lang="en">
<head>
<meta charset="utf-8">
<title>Pruett Design &amp; Millwork</title>
<link href="https://fonts.googleapis.com/css2?family=Open+Sans:wght@300;400;600;700&display=swap" rel="stylesheet">
<style>
:root{
  --red:#c8161d;
  --footer-red:#8e1418;
  --footer-dark:#7a1013;
  --footer-icon:#b3474b;
  --sage:#7e8d70;
  --sage-dark:#5b6c4c;
  --tan:#c9a088;
  --mauve:#bda39a;
  --plum:#6d2740;
  --ink:#333;
  --muted:#666;
  --nav:#444;
  --white:#fff;
  --sky-top:#d8e7f2;
  --sky-bottom:#f3f8fb;
}
*{margin:0;padding:0;box-sizing:border-box}
html,body{width:1200px;height:2330px;overflow:hidden}
body{position:relative;font-family:"Open Sans",Arial,sans-serif;color:var(--ink);background:var(--white)}
.abs{position:absolute}

/* hero */
.hero-photo{left:0;top:0;width:1200px;height:788px;
  background:linear-gradient(180deg,#e7c69a 0%,#d7a46e 35%,#a8582b 62%,#6e3116 100%)}
.site-header{left:47px;top:40px;width:1130px;height:130px;background:var(--white);box-shadow:0 2px 6px rgba(0,0,0,.15)}
.brand-plate{left:0;top:0;width:400px;height:130px;background:#e9e9e9;clip-path:polygon(0 0,100% 0,82% 100%,0 100%)}
.brand{left:26px;top:38px;display:flex;align-items:center;gap:12px}
.brand-mark{width:48px;height:48px;background:var(--red)}
.brand-name{font-size:20px;font-weight:700;color:var(--red);line-height:1.1;width:150px}
.top-contact{right:30px;top:28px;display:flex;align-items:center;gap:26px;font-size:14px;color:#777}
.top-contact span{display:flex;align-items:center;gap:6px}
.search-btn{width:28px;height:28px;background:var(--red);display:flex;align-items:center;justify-content:center}
.main-nav{right:30px;top:84px;display:flex;gap:52px;font-size:15px;color:var(--nav);text-transform:uppercase}
.hero-title{left:145px;top:588px;font-size:41px;font-weight:400;color:var(--white);letter-spacing:.5px;text-shadow:0 2px 4px rgba(0,0,0,.35)}
.slider-arrows{left:143px;top:668px;display:flex;gap:5px}
.slider-arrows span{width:26px;height:26px;background:var(--white);display:flex;align-items:center;justify-content:center}
.view-project{left:927px;top:659px;width:133px;height:38px;background:var(--red);color:var(--white);font-size:15px;text-align:center;line-height:38px;text-transform:uppercase}

/* intro boxes */
.about-box{left:142px;top:706px;width:576px;height:186px;background:var(--sage);color:var(--white);padding:16px 24px}
.why-box{left:718px;top:706px;width:342px;height:186px;background:var(--tan);color:var(--white);padding:16px 24px}
.box-title{font-size:27px;font-weight:400;margin-bottom:8px}
.box-title b{font-weight:700}
.box-text{font-size:14px;line-height:24px}
.read-more{left:163px;top:892px;width:105px;height:35px;background:var(--sage-dark);color:var(--white);font-size:14px;text-align:center;line-height:35px}

/* portfolio */
.portfolio-title{left:152px;top:970px;font-size:37px;font-weight:400;color:var(--plum)}
.portfolio-title b{font-weight:700}
.portfolio-sub{left:152px;top:1025px;font-size:15px;color:var(--muted)}
.tab{top:1097px;height:33px;font-size:13px;line-height:33px;text-align:center}
.tab-active{left:160px;width:123px;background:var(--mauve);color:var(--white);font-weight:600}
.tab-idle{left:285px;width:138px;background:#e4e4e4;color:#555}
.portfolio-band{left:0;top:1130px;width:1200px;height:263px;background:var(--mauve)}
.thumb{top:1165px;width:273px;height:182px;border:5px solid #f3ecea;
  background:linear-gradient(160deg,#f6efe6 0%,#c98a55 55%,#8a3d1a 100%)}

/* what we do */
.services{left:0;top:1393px;width:1200px;height:420px;background:linear-gradient(180deg,var(--sky-top),var(--sky-bottom))}
.section-title{width:1200px;left:0;text-align:center;font-size:24px;font-weight:600;color:#222}
.services-intro{left:145px;top:1472px;width:910px;text-align:center;font-size:17px;line-height:24px;color:#555}
.house-art{left:240px;top:1545px;width:400px;height:350px;border-radius:6px;
  background:linear-gradient(180deg,#e3ebf0 0%,#b9bec2 30%,#9a9a98 55%,#8f7a5e 72%,#7d9a5a 86%,#5f7f40 100%)}
.service-list{left:645px;top:1572px;list-style:none;font-size:14px;color:#555}
.service-list li{height:34px;display:flex;align-items:center;gap:14px}

/* testimonials */
.quote-text{left:205px;top:2012px;width:790px;text-align:center;font-size:13px;line-height:23px;color:#555}
.quote-mark{font-size:90px;color:#d6d6d6;font-family:Georgia,serif;line-height:1}
.client-name{left:0;width:1200px;top:2110px;text-align:center;font-size:13px;color:var(--red)}

/* footer */
.site-footer{left:0;top:2185px;width:1200px;height:145px;background:var(--footer-red);color:var(--white)}
.footer-contact{top:32px;display:flex;align-items:center;gap:14px;font-size:25px}
.circle{width:56px;height:56px;border-radius:50%;background:var(--footer-dark);display:flex;align-items:center;justify-content:center}
.footer-links{left:160px;top:103px;display:flex;gap:26px;font-size:13px}
.copyright{right:142px;top:103px;font-size:13px;font-weight:600}
</style>
</head>
<body>

<div class="abs hero-photo" role="img" aria-label="Photo of a warm hardwood entry hall with a white and oak staircase"></div>

<header class="abs site-header">
  <div class="abs brand-plate"></div>
  <div class="abs brand"><div class="brand-mark"></div><div class="brand-name">Pruett Design &amp; Millwork</div></div>
  <div class="abs top-contact">
    <span><svg width="14" height="14" viewBox="0 0 14 14"><path d="M3 1l2 3-1.5 1.5a8 8 0 004.9 4.9L10 9l3 2-1.5 2.5C6 13 1 8 0.5 2.5z" fill="#888"/></svg>1300 555 014</span>
    <span><svg width="16" height="10" viewBox="0 0 16 10"><rect x=".5" y=".5" width="15" height="9" fill="none" stroke="#888"/><path d="M.5 .5l7.5 5 7.5-5" fill="none" stroke="#888"/></svg>contact@pruettdesign.com.au</span>
    <span class="search-btn"><svg width="14" height="14" viewBox="0 0 14 14"><circle cx="6" cy="6" r="4" fill="none" stroke="#fff" stroke-width="2"/><path d="M9 9l4 4" stroke="#fff" stroke-width="2"/></svg></span>
  </div>
  <nav class="abs main-nav"><span>Home</span><span>About Us</span><span>Services</span><span>Portfolio</span><span>Contact Us</span></nav>
</header>

<h1 class="abs hero-title">OREM IPSUM DOLOR SIT AMET CONSECTETUR</h1>
<div class="abs slider-arrows">
  <span><svg width="10" height="12" viewBox="0 0 10 12"><path d="M7 1L2 6l5 5" fill="none" stroke="#333" stroke-width="2"/></svg></span>
  <span><svg width="10" height="12" viewBox="0 0 10 12"><path d="M3 1l5 5-5 5" fill="none" stroke="#333" stroke-width="2"/></svg></span>
</div>
<div class="abs view-project">View Project</div>

<section class="abs about-box">
  <h2 class="box-title">About <b>PruettDesign</b> and <b>Millwork</b></h2>
  <p class="box-text">Lorem ipsum dolor sit amet, consectetur adipiscing elit. Duis auctor erat eget lobortis dictum. Mauris dolor felis, rutrum quis elit ut, adipiscing accumsan nulla. Suspendisse neque velit, faucibus quis imperdiet a, blandit sit amet dolor.</p>
</section>
<section class="abs why-box">
  <h2 class="box-title"><b>Why we are the best</b></h2>
  <p class="box-text">Lorem ipsum dolor sit amet, consectetur adipiscing elit. Duis auctor erat eget lobortis dictum. Mauris dolor felis, rutrum quis elit ut, adipiscing accumsan nulla.</p>
</section>
<div class="abs read-more">Read more</div>

<h2 class="abs portfolio-title">Latest <b>portfolio</b> projects</h2>
<p class="abs portfolio-sub">Lorem ipsum dolor sit amet, consectetur adipiscing elit. Nulla id congue mi, sed placerat</p>
<div class="abs tab tab-active">Our Millwork</div>
<div class="abs tab tab-idle">My House Designs</div>
<div class="abs portfolio-band"></div>
<div class="abs thumb" style="left:158px" role="img" aria-label="Millwork project photo of a curved oak staircase"></div>
<div class="abs thumb" style="left:463px" role="img" aria-label="Millwork project photo of a curved oak staircase"></div>
<div class="abs thumb" style="left:768px" role="img" aria-label="Millwork project photo of a curved oak staircase"></div>

<section class="abs services"></section>
<h2 class="abs section-title" style="top:1436px">What We Do</h2>
<p class="abs services-intro">Lorem ipsum dolor sit amet, consectetur adipiscing elit. Duis auctor erat eget lobortis dictum. Mauris dolor felis, rutrum Quis elit ut, adipiscing accumsan nulla. Suspendisse neque velit</p>
<div class="abs house-art" role="img" aria-label="Architectural sketch of a modern two-storey house with timber cladding on a grassy lot"></div>
<ul class="abs service-list">
  <li><svg width="6" height="8" viewBox="0 0 6 8"><path d="M0 0l6 4-6 4z" fill="#999"/></svg>Lorem ipsum dolor sit amet.</li>
  <li><svg width="6" height="8" viewBox="0 0 6 8"><path d="M0 0l6 4-6 4z" fill="#999"/></svg>consectetur adipiscing elit.</li>
  <li><svg width="6" height="8" viewBox="0 0 6 8"><path d="M0 0l6 4-6 4z" fill="#999"/></svg>Duis auctor erat eget lobortis dictum.</li>
  <li><svg width="6" height="8" viewBox="0 0 6 8"><path d="M0 0l6 4-6 4z" fill="#999"/></svg>Mauris dolor felis, rutrum, adipiscing accumsan nulla.</li>
  <li><svg width="6" height="8" viewBox="0 0 6 8"><path d="M0 0l6 4-6 4z" fill="#999"/></svg>Suspendisse neque velit, faucibus quis imperdiet a.</li>
  <li><svg width="6" height="8" viewBox="0 0 6 8"><path d="M0 0l6 4-6 4z" fill="#999"/></svg>blandit sit amet doloc</li>
</ul>

<h2 class="abs section-title" style="top:1958px;font-size:23px">Happy Clients</h2>
<span class="abs quote-mark" style="left:150px;top:1995px">&ldquo;</span>
<p class="abs quote-text">Lorem ipsum dolor sit amet, consectetur adipisicing elit, sed do eiusmod tempor incididunt ut labore et dolore magna aliqua. Ut enim ad minim veniam, quis nostrud exercitation ullamco laboris nisi ut aliquip ex ea commodo consequat. Duis aute irure dolor in reprehenderit in voluptate velit esse cillum dolore eu fugiat nulla pariatur. Excepteur sint occaecat cupidatat non proident, sunt in culpa qui officia deserunt mollit anim id est laborum.</p>
<span class="abs quote-mark" style="left:1005px;top:2078px">&rdquo;</span>
<p class="abs client-name">Marla Kestrel</p>

<footer class="abs site-footer">
  <div class="abs footer-contact" style="left:160px">
    <span class="circle"><svg width="22" height="22" viewBox="0 0 14 14"><path d="M3 1l2 3-1.5 1.5a8 8 0 004.9 4.9L10 9l3 2-1.5 2.5C6 13 1 8 0.5 2.5z" fill="var(--footer-icon)"/></svg></span>1300 555 014
  </div>
  <div class="abs footer-contact" style="left:420px">
    <span class="circle"><svg width="24" height="16" viewBox="0 0 16 10"><rect x=".5" y=".5" width="15" height="9" fill="none" stroke="var(--footer-icon)"/><path d="M.5 .5l7.5 5 7.5-5" fill="none" stroke="var(--footer-icon)"/></svg></span>contact@pruettdesign.com.au
  </div>
  <div class="abs footer-contact" style="left:920px;gap:8px">
    <span class="circle"><svg width="24" height="24" viewBox="0 0 24 24" aria-label="Share"><circle cx="6" cy="12" r="3" fill="var(--footer-icon)"/><circle cx="18" cy="6" r="3" fill="var(--footer-icon)"/><circle cx="18" cy="18" r="3" fill="var(--footer-icon)"/><path d="M6 12L18 6M6 12l12 6" stroke="var(--footer-icon)" stroke-width="2"/></svg></span>
    <span class="circle"><svg width="24" height="24" viewBox="0 0 24 24" aria-label="Link"><rect x="2" y="8" width="12" height="8" rx="4" fill="none" stroke="var(--footer-icon)" stroke-width="2.2"/><rect x="10" y="8" width="12" height="8" rx="4" fill="none" stroke="var(--footer-icon)" stroke-width="2.2"/></svg></span>
  </div>
  <nav class="abs footer-links"><span>Home</span><span>About Us</span><span>Services</span><span>Portfolio</span><span>Contact Us</span></nav>
  <p class="abs copyright">Copyright © 2014 - PruettDesign and Millwork</p>
</footer>

</body>
</html>
```